Corporate Design Update für K7-Technik GmbH
Zielgruppe
Mein Unternehmen erbringt Dienstleistungen rund um BHKW-Anlagen, Energieerzeugung, -Transport und -Verteilung. Zusätzlich werden CAD Dienstleistungen für Mechanik und Elektrotechnik angeboten.
Aufgabenstellung
Der Unternehmenssitz wird verlegt und benötigt somit einige Änderungen im Corporate design. Gerne möchte ich das vorhandene verändern und in ein neues design überführen.

```html
<!DOCTYPE html>
<html lang="de">
<head>
<meta charset="utf-8">
<title>K7-Technik GmbH – Geschäftsausstattung</title>
<link href="https://fonts.googleapis.com/css2?family=Montserrat:wght@600;700&family=Roboto:wght@400;500&display=swap" rel="stylesheet">
<style>
  :root{
    --blue:#1a8fd3;
    --navy:#1b2331;
    --grey:#5b5d61;
    --faint:#e6e7e9;
    --paper:#ffffff;
    --board-a:#f4f4f3;
    --board-b:#e7e7e5;
    --text:#3a3b3e;
  }
  *{box-sizing:border-box;margin:0;padding:0}
  html,body{width:1200px;height:1200px;overflow:hidden;background:#fff}
  body{position:relative;font-family:"Roboto",Arial,sans-serif;color:var(--text)}
  .board{position:absolute;left:164px;top:11px;width:882px;height:1175px;
    background:linear-gradient(180deg,var(--board-a),var(--board-b))}
  .item{position:absolute;background:var(--paper);box-shadow:2px 3px 6px rgba(0,0,0,.25);overflow:hidden}
  .item.dark{background:var(--navy)}
  .label{position:absolute;font-size:12px;color:#333;font-family:"Roboto",Arial,sans-serif}
  .brand{position:absolute;font-family:"Montserrat",Arial,sans-serif;font-weight:700;color:var(--blue);
    white-space:nowrap;display:flex;align-items:center;gap:.35em;line-height:1}
  .brand::before{content:"";width:.8em;height:.8em;background:currentColor;display:block}
  .brand.plain::before{display:none}
  .brand.faint{color:var(--faint)}
  .brand.light{color:#fff}
  .brand.muted{color:#a9abae}
  .small{font-size:4.6px;line-height:1.4;position:absolute;white-space:nowrap}
  .role{position:absolute;text-align:right;font-size:4.8px;line-height:1.35}
  .role b{font-family:"Montserrat",Arial,sans-serif;color:var(--blue);font-weight:700;display:block}
  .dark .role,.dark .small{color:#fff}
  .contacts{position:absolute;font-size:4.2px;line-height:1.45;list-style:none;white-space:nowrap}
  .contacts li{display:flex;gap:3px;align-items:center}
  .contacts li::before{content:"";width:3px;height:3px;border-radius:50%;background:currentColor;flex:none}
  .contacts li.cont::before{visibility:hidden}
  .dark .contacts{color:#fff}
  .web{position:absolute;font-size:7px;letter-spacing:3px;color:#fff;white-space:nowrap}
  .band{position:absolute;background:var(--blue)}
</style>
</head>
<body>
<div class="board">

  <section class="item letterhead" style="left:75px;top:80px;width:350px;height:495px">
    <div class="brand" style="left:14px;top:24px;font-size:15px">K7-Technik GmbH</div>
    <div class="small" style="right:14px;top:24px;text-align:right">Ahornweg 9<br>D-70173 Musterstadt</div>
    <div class="small" style="right:14px;top:38px;text-align:right">+49 (0)711-40 18 22 10<br>+49 (0)711-40 18 22 12<br>+49 (0)170-55 31 904<br>jhe@k7-technik.de<br>www.k7-technik.de</div>
    <div class="small" style="left:23px;top:89px;letter-spacing:.3px"><b>K7-Technik GmbH</b> &nbsp;| &nbsp;Ahornweg 9 - D-70173 Musterstadt</div>
    <div style="position:absolute;left:0;top:173px;width:12px;border-top:1px solid #999"></div>
    <div style="position:absolute;left:0;top:246px;width:12px;border-top:1px solid #999"></div>
    <div style="position:absolute;left:0;top:346px;width:12px;border-top:1px solid #999"></div>
    <div class="small" style="left:11px;top:453px">Sitz der Gesellschaft<br>Registergericht Musterstadt<br>Geschäftsführer<br>Handelsregister-Nr<br>USt-ID-Nr</div>
    <div class="small" style="left:80px;top:453px">Musterstadt<br><br>Jonas Hellwig<br>HRB 402117<br>DE301447288</div>
    <div style="position:absolute;left:142px;top:453px;height:30px;border-left:1px solid #888"></div>
    <div class="small" style="left:155px;top:453px">Bank<br><br>IBAN<br>BIC</div>
    <div class="small" style="left:179px;top:453px">Finanzamt Musterstadt Bankverbindung<br>Regiobank Südwest eG<br>DE12 3456 0000 0007 8901 23<br>RGSWDE66</div>
    <div class="brand muted plain" style="right:8px;top:470px;font-size:9px">K7-Technik</div>
    <div class="band" style="left:0;bottom:0;width:290px;height:6px;clip-path:polygon(0 0,96% 0,100% 100%,0 100%)"></div>
  </section>

  <section class="item" style="left:464px;top:77px;width:377px;height:171px;box-shadow:none">
    <div class="brand" style="left:46px;top:72px;font-size:19px;flex-direction:column;gap:6px">K7-Technik<span style="font-size:10px;color:var(--grey)">GmbH</span></div>
    <div class="brand" style="left:210px;top:78px;font-size:14px">K7-Technik GmbH</div>
  </section>
  <section class="item dark" style="left:464px;top:285px;width:377px;height:171px;box-shadow:none">
    <div class="brand" style="left:44px;top:72px;font-size:19px;flex-direction:column;gap:6px">K7-Technik<span style="font-size:10px;color:#fff">GmbH</span></div>
    <div class="brand" style="left:210px;top:78px;font-size:14px">K7-Technik GmbH</div>
  </section>

  <div class="label" style="left:453px;top:490px">1</div>
  <section class="item" style="left:466px;top:489px;width:367px;height:184px">
    <div class="brand" style="left:8px;top:25px;font-size:13px">K7-Technik GmbH</div>
    <div class="brand faint plain" style="left:205px;top:80px;font-size:40px">K7</div>
    <div class="band" style="left:0;bottom:0;width:290px;height:13px;clip-path:polygon(0 0,95% 0,100% 100%,0 100%)"></div>
    <div class="web" style="left:142px;bottom:2px">www.k7-technik.de</div>
  </section>

  <div class="label" style="left:453px;top:706px">2</div>
  <section class="item dark" style="left:466px;top:703px;width:367px;height:183px">
    <div class="brand" style="left:8px;top:25px;font-size:13px">K7-Technik GmbH</div>
    <div style="position:absolute;left:34px;top:81px;width:166px;height:73px;background:#fff;border-radius:4px"></div>
    <div class="brand light plain" style="left:250px;top:100px;font-size:28px">K7</div>
    <div class="web" style="left:232px;top:148px">www.k7-technik.de</div>
  </section>

  <div class="label" style="left:453px;top:922px">3</div>
  <section class="item" style="left:466px;top:918px;width:367px;height:184px">
    <div class="brand" style="left:8px;top:25px;font-size:13px">K7-Technik GmbH</div>
    <div style="position:absolute;left:34px;top:81px;width:166px;height:73px;background:#dcdde0;border-radius:4px"></div>
    <div class="brand muted plain" style="left:250px;top:100px;font-size:28px">K7</div>
    <div class="web" style="left:232px;top:148px;color:#a9abae">www.k7-technik.de</div>
  </section>

  <div class="label" style="left:66px;top:617px">1</div>
  <section class="item" style="left:120px;top:612px;width:93px;height:143px">
    <div class="brand" style="left:10px;top:22px;font-size:9px;flex-direction:column;gap:3px">K7-Technik<span style="font-size:5px;color:var(--grey)">GmbH</span></div>
    <div class="role" style="left:10px;top:62px;text-align:left">Geschäftsführer<b>JONAS HELLWIG</b>Dipl.-Ing. Elektrotechnik</div>
    <ul class="contacts" style="left:8px;top:91px"><li>Ahornweg 9</li><li class="cont">D-70173 Musterstadt</li><li>+49 (0)711-40 18 22 10</li><li>+49 (0)711-40 18 22 12</li><li>+49 (0)170-55 31 904</li><li>jhe@k7-technik.de</li><li>www.k7-technik.de</li></ul>
  </section>

  <div class="label" style="left:260px;top:617px">A</div>
  <section class="item" style="left:278px;top:608px;width:142px;height:92px">
    <div class="brand" style="left:12px;top:14px;font-size:10px">K7-Technik GmbH</div>
    <div class="role" style="right:78px;top:56px;width:60px">Geschäftsführer<b>JONAS HELLWIG</b>Dipl.-Ing. Elektrotechnik</div>
    <ul class="contacts" style="left:72px;top:46px"><li>Ahornweg 9</li><li class="cont">D-70173 Musterstadt</li><li>+49 (0)711-40 18 22 10</li><li>+49 (0)711-40 18 22 12</li><li>+49 (0)170-55 31 904</li><li>jhe@k7-technik.de</li><li>www.k7-technik.de</li></ul>
  </section>

  <div class="label" style="left:66px;top:786px">2</div>
  <section class="item" style="left:93px;top:780px;width:141px;height:92px">
    <div class="brand" style="left:28px;top:34px;font-size:12px;flex-direction:column;gap:4px">K7-Technik<span style="font-size:6px;color:var(--grey)">GmbH</span></div>
  </section>

  <div class="label" style="left:260px;top:727px">B</div>
  <section class="item dark" style="left:275px;top:722px;width:141px;height:92px">
    <div class="brand" style="left:12px;top:14px;font-size:10px">K7-Technik GmbH</div>
    <div class="role" style="right:76px;top:58px;width:60px">Geschäftsführer<b>JONAS HELLWIG</b>Dipl.-Ing. Elektrotechnik</div>
    <ul class="contacts" style="left:72px;top:46px"><li>Ahornweg 9</li><li class="cont">D-70173 Musterstadt</li><li>+49 (0)711-40 18 22 10</li><li>+49 (0)711-40 18 22 12</li><li>+49 (0)170-55 31 904</li><li>jhe@k7-technik.de</li><li>www.k7-technik.de</li></ul>
  </section>

  <div class="label" style="left:66px;top:895px">3</div>
  <section class="item dark" style="left:118px;top:887px;width:91px;height:141px">
    <div class="brand" style="left:12px;top:52px;font-size:9px;flex-direction:column;gap:3px">K7-Technik<span style="font-size:5px;color:#fff">GmbH</span></div>
    <div class="band" style="left:0;bottom:0;width:100%;height:12px"></div>
    <div class="web" style="left:10px;bottom:3px;font-size:5px;letter-spacing:1px">www.k7-technik.de</div>
  </section>

  <div class="label" style="left:260px;top:919px">C</div>
  <section class="item dark" style="left:304px;top:888px;width:92px;height:142px">
    <div class="brand" style="left:12px;top:18px;font-size:9px;flex-direction:column;gap:3px">K7-Technik<span style="font-size:5px;color:#fff">GmbH</span></div>
    <div class="role" style="right:8px;top:55px;font-size:5.2px">Geschäftsführer<b>JONAS HELLWIG</b>Dipl.-Ing. Elektrotechnik</div>
    <ul class="contacts" style="left:8px;top:88px"><li>Ahornweg 9</li><li class="cont">D-70173 Musterstadt</li><li>+49 (0)711-40 18 22 10</li><li>+49 (0)711-40 18 22 12</li><li>+49 (0)170-55 31 904</li><li>jhe@k7-technik.de</li><li>www.k7-technik.de</li></ul>
  </section>

  <div class="label" style="left:66px;top:1045px">4</div>
  <section class="item dark" style="left:93px;top:1040px;width:141px;height:92px">
    <div class="brand" style="left:28px;top:34px;font-size:12px;flex-direction:column;gap:4px">K7-Technik<span style="font-size:6px;color:#fff">GmbH</span></div>
  </section>

</div>
</body>
</html>
```